Flyer - Spec sheet Marine Industry

Design Brief – KRL Anchor Chain Spec Sheet Flyer Redesign

THE FIRST ATTACHMENT IS THE CURRENT DESIGN
THE OTHERS ARE FOR INSPIRATION

Objective

Redesign our current KRL Anchor Chain specification sheet flyer to align with our new Kestrel Marine branding, creating a more premium, high-end marine presentation that reflects our position as Australia’s Marine Chain Specialists.

The new flyer should feel luxury, professional, and visually strong, targeting premium boat owners, marine dealers, OEM clients, shipyards, and superyacht clientele.

Brand Direction

We want the flyer to reflect a premium marine identity with a strong superyacht aesthetic.

Visual style should include:

• Deep navy blue tones
• Crisp white contrast
• Premium metallic silver/steel elements
• Subtle gold accents where suitable
• Clean luxury presentation
• Strong marine/ocean visuals
• Superyacht lifestyle feel
• Premium anchor chain close-up imagery
• High-end industrial meets luxury marine feel

The flyer should feel similar to premium yacht brands rather than industrial wholesale suppliers.

Logo Update

Please remove all old branding and replace with our new Kestrel Marine branding.

New branding to include:

• Kestrel Marine logo
• KRL Anchor Chain branding
• Australia’s Marine Chain Specialists
• Premium positioning around KRL G43 Anchor Chain

Please ensure the logo is prominent and visually balanced throughout the flyer.

Key Messaging to Highlight

Main product focus:

KRL G43 Anchor Chain

Core selling points to highlight:

• 50% Stronger than standard anchor chains
• Certified & Tested
• BLEV Certified / Batch Tested
• Marine Grade Protection
• Thicker galvanised coating for superior corrosion resistance
• Built for Australian marine conditions
• Trusted by premium vessel owners and marine professionals

Tone should feel premium and authoritative, not overly sales-heavy.

Layout Direction

We want a cleaner and more modern layout than the current flyer.

Preferred design approach:

• Less clutter
• Strong hero image of superyacht + anchor chain
• Better use of whitespace
• Cleaner typography
• More premium icon usage
• Strong product hierarchy
• More visual impact
• Easy to read technical specifications
• Better presentation of chain grades and sizing tables

The flyer should work both digitally and in print.

Contact Details to Include

Kestrel Marine
Kestrelmarine-demo.com.au
sales@kestrelmarine-demo.com.au
(07) 5550 1234 / 0491 570 156

Also include partner branding where appropriate:

• TQR Electronics
• Dravolift

Reference Style

Please use our updated ute graphics and recent marketing material as the design reference for the overall brand direction.

We want consistency across:

• Vehicle graphics
• Stubby coolers
• Flags
• Showroom signage
• Flyers
• Product stickers
• Trade show displays

Final Goal

The finished flyer should feel like a premium marine brand brochure that immediately positions Kestrel Marine as the leader in anchor chain supply across Australia.

It should create trust, authority, and strong visual impact from first glance.

```html
<!DOCTYPE html>
<html lang="en">
<head>
<meta charset="utf-8">
<title>Kestrel Marine – KRL Anchor Chain Flyer</title>
<link href="https://fonts.googleapis.com/css2?family=Montserrat:ital,wght@0,500;0,600;0,700;0,800;1,600;1,700;1,800&display=swap" rel="stylesheet">
<style>
  :root {
    --navy: #2a3a96;
    --navy-deep: #1f2c7d;
    --white: #ffffff;
    --ink: #111111;
    --green: #1f9a48;
    --steel: #b9c3cf;
    --page: #e9eaec;
  }
  * { margin: 0; padding: 0; box-sizing: border-box; }
  html, body { width: 707px; height: 1200px; overflow: hidden; }
  body {
    background: var(--page);
    font-family: "Montserrat", sans-serif;
    display: flex; align-items: center; justify-content: center;
  }
  .flyer {
    position: relative; width: 707px; height: 472px;
    background: var(--white); overflow: hidden;
    box-shadow: 0 4px 14px rgba(0,0,0,.25);
  }

  /* brand */
  .brand { position: absolute; left: 38px; top: 24px; }
  .brand-name {
    font-weight: 800; font-size: 38px; line-height: 1; color: var(--navy);
    letter-spacing: -0.5px; text-transform: uppercase;
  }
  .brand-sub {
    margin-top: 6px; font-weight: 700; font-size: 12px; letter-spacing: 3px;
    color: var(--green); text-transform: uppercase;
  }

  /* headline */
  .headline { position: absolute; left: 400px; width: 306px; top: 22px; text-align: center; color: var(--ink); }
  .headline .lead { font-style: italic; font-weight: 600; font-size: 18px; line-height: 1.1; }
  .headline .title { font-weight: 800; font-size: 25px; color: var(--navy); line-height: 1.05; letter-spacing: .2px; }
  .headline .tail { font-style: italic; font-weight: 800; font-size: 19px; line-height: 1.1; }
  .headline .note { margin-top: 5px; font-style: italic; font-weight: 600; font-size: 10px; line-height: 1.1; }
  .headline .note strong { font-weight: 800; }

  /* feature band */
  .feature-band { position: absolute; left: 0; top: 110px; width: 440px; height: 92px; }
  .feature-list { position: absolute; left: 0; top: 110px; width: 420px; display: flex; justify-content: space-around; }
  .feature { width: 130px; text-align: center; color: var(--white); }
  .feature-icon { width: 50px; height: 26px; margin: 0 auto; display: block; }
  .feature-text { margin-top: 12px; font-weight: 600; font-size: 8.6px; line-height: 1.15; text-transform: none; }

  /* bullets */
  .benefits { position: absolute; left: 40px; top: 209px; list-style: none; }
  .benefits li {
    display: flex; align-items: center; gap: 7px; height: 16px;
    font-style: italic; font-weight: 700; font-size: 8.8px; color: var(--ink);
  }
  .benefits svg { width: 10px; height: 10px; flex: none; }

  /* imagery */
  .yacht-photo {
    position: absolute; left: 380px; top: 150px; width: 327px; height: 260px;
    background: linear-gradient(180deg, #ffffff 0%, #eef2f6 45%, #c9d3de 70%, #e3e9ef 100%);
  }
  .chain-photo {
    position: absolute; left: 0; top: 292px; width: 560px; height: 180px;
    background: radial-gradient(ellipse at 30% 60%, #4d87c4 0%, #2f5f9a 45%, #6b4a3c 70%, rgba(255,255,255,0) 90%);
  }
  .chain-inset {
    position: absolute; left: 556px; top: 298px; width: 118px; height: 118px; border-radius: 50%;
    border: 4px solid var(--navy);
    background: radial-gradient(circle, #e1e6ec 0%, #aab4c0 60%, #8893a0 100%);
  }

  /* contact */
  .contact-band { position: absolute; left: 0; top: 0; width: 707px; height: 472px; }
  .contact { position: absolute; right: 30px; top: 407px; list-style: none; text-align: right; }
  .contact li {
    display: flex; justify-content: flex-end; align-items: center; gap: 6px;
    height: 18px; font-style: italic; font-weight: 700; font-size: 11.5px; color: var(--white);
  }
  .contact svg { width: 11px; height: 11px; flex: none; }
</style>
</head>
<body>
<main class="flyer">

  <div class="yacht-photo" role="img" aria-label="White superyacht on calm water, photographed bow-first"></div>
  <div class="chain-photo" role="img" aria-label="Close-up of heavy galvanised anchor chain links with blue and rust tones"></div>

  <svg class="contact-band" viewBox="0 0 707 472" aria-hidden="true">
    <rect x="200" y="404" width="507" height="68" fill="var(--navy)"/>
  </svg>

  <div class="chain-inset" role="img" aria-label="Circular close-up of bright galvanised chain links"></div>

  <header class="brand">
    <div class="brand-name">Kestrel Marine</div>
    <div class="brand-sub">KRL Anchor Chain</div>
  </header>

  <section class="headline">
    <p class="lead">Australia’s</p>
    <h1 class="title">MARINE CHAIN</h1>
    <p class="tail">Specialists</p>
    <p class="note">Premium positioning around<br><strong>KRL G43 Anchor Chain</strong></p>
  </section>

  <svg class="feature-band" viewBox="0 0 440 92" aria-hidden="true">
    <polygon points="0,24 440,24 425,80 0,80" fill="var(--navy)"/>
    <circle cx="70" cy="24" r="25" fill="var(--navy)"/>
    <circle cx="205" cy="24" r="25" fill="var(--navy)"/>
    <circle cx="336" cy="24" r="25" fill="var(--navy)"/>
  </svg>

  <ul class="feature-list">
    <li class="feature">
      <svg class="feature-icon" viewBox="0 0 50 26" fill="none" stroke="#fff" stroke-width="1.4">
        <path d="M17 20h16M20 20v-8h6l3-6v14M22 10l2-2"/>
      </svg>
      <p class="feature-text">50% STRONGER<br>than standard<br>anchor chains</p>
    </li>
    <li class="feature">
      <svg class="feature-icon" viewBox="0 0 50 26" fill="none" stroke="#fff" stroke-width="1.4">
        <circle cx="25" cy="12" r="8"/><path d="M21 12l3 3 5-6M20 19l-3 6M30 19l3 6"/>
      </svg>
      <p class="feature-text">CERTIFIED &amp; TESTED<br>BLEV Certified/<br>Batch Tested</p>
    </li>
    <li class="feature">
      <svg class="feature-icon" viewBox="0 0 50 26" fill="none" stroke="#fff" stroke-width="1.4">
        <path d="M25 3l8 3v7c0 5-4 8-8 10-4-2-8-5-8-10V6z"/><path d="M21 13l3 3 5-6"/>
      </svg>
      <p class="feature-text">MARINE GRADE<br>PROTECTION</p>
    </li>
  </ul>

  <ul class="benefits">
    <li><svg viewBox="0 0 10 10"><circle cx="5" cy="5" r="5" fill="var(--green)"/><path d="M2.8 5.2l1.5 1.5 3-3" stroke="#fff" stroke-width="1.3" fill="none"/></svg>Thicker galvanised coating for superior corrosion resistance</li>
    <li><svg viewBox="0 0 10 10"><circle cx="5" cy="5" r="5" fill="var(--green)"/><path d="M2.8 5.2l1.5 1.5 3-3" stroke="#fff" stroke-width="1.3" fill="none"/></svg>Built for Australian marine conditions</li>
    <li><svg viewBox="0 0 10 10"><circle cx="5" cy="5" r="5" fill="var(--green)"/><path d="M2.8 5.2l1.5 1.5 3-3" stroke="#fff" stroke-width="1.3" fill="none"/></svg>Trusted by premium vessel owners and marine professionals</li>
  </ul>

  <ul class="contact">
    <li><svg viewBox="0 0 12 12" fill="none" stroke="#fff" stroke-width="1"><circle cx="6" cy="6" r="5"/><ellipse cx="6" cy="6" rx="2.2" ry="5"/><path d="M1 6h10"/></svg>www.kestrelmarine-demo.com.au</li>
    <li><svg viewBox="0 0 12 12" fill="none" stroke="#fff" stroke-width="1"><rect x="1" y="2.5" width="10" height="7"/><path d="M1 2.5l5 4 5-4"/></svg>sales@kestrelmarine-demo.com.au</li>
    <li><svg viewBox="0 0 12 12" fill="none" stroke="#fff" stroke-width="1.2"><path d="M2 1.5l2.2 0 1 2.6-1.3 1a6 6 0 0 0 3 3l1-1.3 2.6 1v2.2c-5 .5-9-3.5-8.5-8.5z"/></svg>(07) 5550 1234 / 0491 570 156</li>
  </ul>

</main>
</body>
</html>
```